Business Card Design

Cake decorating business in a small town in Australia. looking for a style that is fresh with a touch of vintage/country. liking these ideas, timber backgrounds, chalkboards, bunting, flowers and cake elements (rolling pins, cupcakes, cake stands, etc.) would consider a shot saying/statement. would like the back of the card to have wording "Specialising in delectable treats for all your special occasions" - wedding cakes - birthday cakes - special occasion cakes - novelty cakes - cupcakes, cookies, slices and cake pops. maybe incorporate a cake in design on back page. attached are a few of my favourite cakes and the start of a card design I liked.

Industry/Entity Type

Business

Contact Information for Business Card

Marigold's Sugarloft Bakes 0438 056 969Find me on (Chirpwall Logo)

Requirements
Nice to have
• timber, some of my designs, chalkboard, baking utensils
Should not have
• no red font

```html
<!DOCTYPE html>
<html lang="en">
<head>
<meta charset="utf-8">
<title>Business Card Back – Specialty Cakes</title>
<link rel="stylesheet" href="https://fonts.googleapis.com/css2?family=Architects+Daughter&family=Carlito&display=swap">
<style>
  :root {
    --timber-light: #e9c894;
    --timber-mid: #d9ad6e;
    --timber-deep: #c99350;
    --ink: #1c1712;
    --pink-cake: #d98aa0;
    --pink-cake-deep: #8f6a5c;
    --chocolate: #5a3524;
    --chocolate-light: #b48a6a;
    --pops-blue: #5a9fc9;
    --pops-pink: #c98a94;
    --pram-dark: #2a2622;
    --pram-cream: #e6ddd2;
    --cupcake-cream: #efe6dc;
    --cupcake-brown: #6a4a36;
  }
  * { box-sizing: border-box; margin: 0; padding: 0; }
  html, body {
    width: 1200px;
    height: 727px;
    overflow: hidden;
    background: #ffffff;
  }
  .card-back {
    position: relative;
    width: 1200px;
    height: 727px;
    overflow: hidden;
    background:
      linear-gradient(90deg, rgba(255,255,255,0.08) 0%, rgba(0,0,0,0.04) 20%, rgba(255,255,255,0.1) 45%, rgba(0,0,0,0.05) 70%, rgba(255,255,255,0.06) 100%),
      linear-gradient(180deg, var(--timber-light) 0%, var(--timber-mid) 55%, var(--timber-deep) 100%);
  }
  .tagline {
    position: absolute;
    left: 40px;
    top: 40px;
    font-family: "Architects Daughter", cursive;
    font-size: 35px;
    color: var(--ink);
    white-space: nowrap;
    letter-spacing: 0.2px;
  }
  .services {
    position: absolute;
    left: 64px;
    top: 190px;
    list-style: none;
    font-family: "Carlito", sans-serif;
    font-size: 32px;
    color: var(--ink);
  }
  .services li {
    position: absolute;
    left: 0;
    white-space: nowrap;
  }
  .services li::before {
    content: "";
    position: absolute;
    left: 0;
    top: 13px;
    width: 13px;
    height: 13px;
    border-radius: 50%;
    background: var(--ink);
  }
  .services li span { position: absolute; left: 82px; }
  .services .item-birthday { top: 0; }
  .services .item-wedding { top: 94px; }
  .services .item-occasion { top: 188px; }
  .services .item-novelty { top: 278px; }
  .services .item-novelty span { left: 88px; }
  .services .item-treats { top: 372px; }
  .services .item-treats span { left: 96px; }

  .cake-photo {
    position: absolute;
    border: 3px solid rgba(255,255,255,0.85);
  }
  .photo-tiered {
    left: 720px; top: 116px; width: 208px; height: 214px;
    background: linear-gradient(180deg, #e7dde0 0%, var(--pink-cake) 45%, var(--pink-cake-deep) 100%);
  }
  .photo-chocolate {
    left: 957px; top: 100px; width: 189px; height: 246px;
    background: linear-gradient(180deg, #f4f0ec 0%, var(--chocolate-light) 30%, var(--chocolate) 75%, #efe9e4 100%);
  }
  .photo-pops {
    left: 981px; top: 370px; width: 147px; height: 150px;
    background: linear-gradient(180deg, var(--pops-blue) 0%, var(--pops-pink) 55%, #7b6a8a 100%);
  }
  .photo-pram {
    left: 772px; top: 428px; width: 183px; height: 210px;
    background: radial-gradient(ellipse at 50% 55%, var(--pram-cream) 0%, #b7aea6 40%, var(--pram-dark) 75%);
  }
  .photo-cupcake {
    left: 997px; top: 544px; width: 131px; height: 183px;
    background: linear-gradient(180deg, var(--cupcake-cream) 0%, #e9c6cf 40%, var(--cupcake-brown) 80%);
  }
</style>
</head>
<body>
  <main class="card-back">
    <p class="tagline">Specialising in delectable treats for all your special occasions</p>

    <ul class="services">
      <li class="item-birthday"><span>birthday cakes</span></li>
      <li class="item-wedding"><span>wedding cakes</span></li>
      <li class="item-occasion"><span>special occasion cakes</span></li>
      <li class="item-novelty"><span>novelty cakes</span></li>
      <li class="item-treats"><span>cupcakes, cookies, slices and cake pops</span></li>
    </ul>

    <div class="cake-photo photo-tiered" role="img" aria-label="Photo of a topsy-turvy three-tier pink and green cake with sugar roses"></div>
    <div class="cake-photo photo-chocolate" role="img" aria-label="Photo of a tiered chocolate cake with cascading chocolate decorations"></div>
    <div class="cake-photo photo-pops" role="img" aria-label="Photo of a bouquet of pink and brown cake pops in a blue pot"></div>
    <div class="cake-photo photo-pram" role="img" aria-label="Photo of a novelty pram cake in white and pink on a dark background"></div>
    <div class="cake-photo photo-cupcake" role="img" aria-label="Photo of a cupcake with swirled frosting and sprinkles"></div>
  </main>
</body>
</html>
```